Corvell Health Booklet 2016

Corvell Health is a multi-specialty Practice in Midtown Manhattan offering advanced care in multiple areas of medicine. See our table of contents (PDF Uploaded)
Our designed booklet should be clean, easy to read, contemporary, high-end and elegant.
We need a general theme, Layout for cover and templates for internal.
We are entertaining the idea of two different sizes
8 x 10
or
11 x 8.5
Our tagline " The Future of Medicine is Here"
We will provide all the text content
The link to our website
www.CorvellHX.com
Uploaded files are as follows.. Logo, Our Team Photo and the PDF listing the table of contents.

```html
<!DOCTYPE html>
<html lang="en">
<head>
<meta charset="utf-8">
<title>Corvell Health Booklet</title>
<link href="https://fonts.googleapis.com/css2?family=Lato:ital,wght@0,300;0,400;0,700;0,900;1,400&display=swap" rel="stylesheet">
<style>
:root{
  --navy:#1d1450;
  --navy-deep:#140d3a;
  --gold:#d9a032;
  --gold-dark:#9a6414;
  --gold-light:#f2c766;
  --paper:#f4f4f7;
  --ink:#3a3a44;
  --stage:#141416;
  --white:#ffffff;
}
*{margin:0;padding:0;box-sizing:border-box}
html,body{width:1200px;height:960px;overflow:hidden;background:var(--stage);font-family:"Lato",sans-serif}
.canvas{position:relative;width:1200px;height:960px}
.page{position:absolute;overflow:hidden}
.page > svg.bg{position:absolute;inset:0;width:100%;height:100%}
.cover{left:36px;top:29px;width:571px;height:441px}
.title-page{left:607px;top:29px;width:572px;height:441px}
.welcome-page{left:36px;top:482px;width:574px;height:443px;background:var(--paper)}
.services-page{left:610px;top:482px;width:573px;height:443px;background:var(--paper)}

.brand{position:absolute;text-align:center;transform:translateX(-50%)}
.brand .dot{display:block;margin:0 auto;border-radius:50%;background:var(--gold)}
.brand .rule{display:block;margin:0 auto;height:2px}
.brand .name{display:block;text-transform:uppercase;font-weight:400;line-height:1.05;letter-spacing:.02em}

.cover .brand{left:285px;top:80px}
.cover .dot{width:80px;height:80px;box-shadow:0 0 0 6px var(--navy-deep)}
.cover .rule{width:150px;background:rgba(255,255,255,.8);margin-top:12px;margin-bottom:12px}
.cover .name{font-size:26px;color:var(--navy)}
.cover-contact{position:absolute;left:0;width:100%;text-align:center;color:var(--white);font-weight:900;text-shadow:0 0 3px var(--navy),0 0 3px var(--navy),0 0 2px var(--navy)}
.cover-address{top:250px;font-size:16px}
.cover-phone{top:288px;font-size:16px;line-height:1.15}
.cover-url{top:345px;font-size:15px}

.title-page .brand{left:138px;top:38px}
.title-page .dot{width:72px;height:72px}
.title-page .rule{width:120px;background:rgba(255,255,255,.7);margin-top:10px;margin-bottom:12px}
.title-page .name{font-size:25px;color:var(--white)}
.tagline{position:absolute;left:370px;top:368px;color:var(--white);font-weight:300;line-height:.92;text-shadow:0 1px 3px rgba(0,0,0,.35)}
.tagline .small{font-size:21px}
.tagline .big{font-size:31px}
.side-url{position:absolute;right:2px;top:330px;writing-mode:vertical-rl;font-size:9px;color:rgba(255,255,255,.75);letter-spacing:.02em}

.welcome-head{position:absolute;left:50px;top:26px;color:var(--white);font-style:italic}
.welcome-head .kicker{display:block;font-size:15px}
.welcome-head .title{display:block;font-size:22px}
.inner-brand{top:66px}
.inner-brand .dot{width:34px;height:34px;box-shadow:0 0 0 3px var(--navy)}
.inner-brand .name{font-size:11px;color:var(--navy);margin-top:6px}
.welcome-page .inner-brand{left:470px}
.services-page .inner-brand{left:489px;top:68px}

.letter{position:absolute;left:27px;top:148px;width:525px;font-size:7px;line-height:9.5px;color:#55555f}
.letter p{margin-bottom:8px}
.letter p.narrow{width:360px}
.letter strong{color:#222;font-weight:700}
.signoff{position:absolute;left:27px;top:404px;color:var(--navy)}
.signoff .sig-name{display:block;font-style:italic;font-size:12px}
.signoff .sig-role{display:block;font-style:italic;font-size:8px;color:#333}
.badges{position:absolute;left:180px;top:403px;width:237px;height:34px;border:1px solid #c9c9cf;background:var(--white);display:flex;align-items:center;justify-content:space-around;padding:0 8px}
.badge{display:block;background:#cfcfd6}
.badge.shield{width:10px;height:12px;background:#8b1d24}
.badge.bar{width:50px;height:8px}
.badge.round{width:12px;height:12px;border-radius:50%;background:#5b2c8a}
.badge.square{width:13px;height:13px;background:var(--navy)}
.portrait{position:absolute;left:452px;top:363px;width:62px;height:76px;border:2px solid #5aa6d6;background:linear-gradient(180deg,#e9eef4,#c7ccd6)}

.services-title{position:absolute;left:91px;top:18px;font-size:36px;font-style:italic;color:var(--white)}
.service{position:absolute;left:50px;width:340px;color:var(--ink)}
.service h3{font-size:15.5px;font-weight:400;color:#1b1b22;margin-bottom:9px}
.service p{font-size:12.5px;line-height:16px;font-weight:300;color:#2c2c34}
.service-1{top:146px}
.service-2{top:234px}
.service-3{top:322px}
.services-photo{position:absolute;left:390px;top:156px;width:185px;height:240px;border:3px solid var(--white);background:linear-gradient(160deg,#ffffff,#dcdde2 55%,#c0b39a)}
.url-band{position:absolute;left:400px;bottom:8px;width:180px;height:14px}
.url-band span{position:absolute;left:38px;top:1px;font-size:8px;color:var(--gold-light)}
</style>
</head>
<body>
<div class="canvas">

  <!-- Front cover -->
  <section class="page cover">
    <svg class="bg" viewBox="0 0 571 441" role="img" aria-label="Night photograph of a lit suspension bridge over a river with the city skyline reflected in the water">
      <defs>
        <linearGradient id="nightSky" x1="0" y1="0" x2="1" y2="1">
          <stop offset="0" stop-color="#3b4a9a"/>
          <stop offset=".35" stop-color="#c9b6e0"/>
          <stop offset=".6" stop-color="#4f5fb0"/>
          <stop offset="1" stop-color="#1a2a6a"/>
        </linearGradient>
      </defs>
      <rect width="571" height="441" fill="url(#nightSky)"/>
    </svg>
    <div class="brand">
      <span class="dot"></span>
      <span class="rule"></span>
      <span class="name">Corvell<br>Health</span>
    </div>
    <p class="cover-contact cover-address">210 E. 48th Street New York, NY 10017</p>
    <p class="cover-contact cover-phone">Phone: 212-555-0148<br>Fax: 212-555-0193</p>
    <p class="cover-contact cover-url">www.CorvellHX.com</p>
  </section>

  <!-- Title page -->
  <section class="page title-page">
    <svg class="bg" viewBox="0 0 572 441">
      <defs>
        <linearGradient id="goldBand" x1="0" y1="0" x2="1" y2="0">
          <stop offset="0" stop-color="#b97a1c"/>
          <stop offset=".5" stop-color="#f0c462"/>
          <stop offset="1" stop-color="#c98a24"/>
        </linearGradient>
        <linearGradient id="clinicPhoto" x1="0" y1="0" x2="1" y2="1">
          <stop offset="0" stop-color="#6b5a4a"/>
          <stop offset=".45" stop-color="#d8d6d2"/>
          <stop offset="1" stop-color="#f1f1f3"/>
        </linearGradient>
      </defs>
      <rect width="572" height="441" fill="var(--navy)"/>
      <rect x="410" y="22" width="140" height="120" rx="16" fill="none" stroke="rgba(255,255,255,.05)" stroke-width="3"/>
      <path d="M0,196 C130,262 260,270 380,222 S520,176 572,186 L572,441 L0,441Z" fill="url(#goldBand)"/>
      <path d="M0,232 C130,292 260,300 380,250 S520,206 572,212 L572,441 L0,441Z" fill="url(#clinicPhoto)" role="img" aria-label="Photograph of a doctor performing an ultrasound on a patient lying on an examination table"/>
    </svg>
    <div class="brand">
      <span class="dot"></span>
      <span class="rule"></span>
      <span class="name">Corvell<br>Health</span>
    </div>
    <p class="tagline"><span class="small">The </span><span class="big">Future</span><span class="small"> of</span><br><span class="big">Medicine</span><span class="small"> is Here</span></p>
    <p class="side-url">www.CorvellHX.com</p>
  </section>

  <!-- Welcome page -->
  <section class="page welcome-page">
    <svg class="bg" viewBox="0 0 574 443">
      <defs>
        <linearGradient id="goldBand2" x1="0" y1="0" x2="1" y2="0">
          <stop offset="0" stop-color="#b97a1c"/>
          <stop offset=".45" stop-color="#f0c462"/>
          <stop offset="1" stop-color="#c98a24"/>
        </linearGradient>
      </defs>
      <path d="M0,58 C90,120 180,128 290,80 S500,50 574,82 L574,0 L0,0Z" fill="url(#goldBand2)"/>
      <path d="M0,58 C80,96 170,100 280,58 S490,40 574,70 L574,0 L0,0Z" fill="var(--navy)"/>
    </svg>
    <h2 class="welcome-head"><span class="kicker">Welcome</span><span class="title">Corvell Health</span></h2>
    <div class="brand inner-brand">
      <span class="dot"></span>
      <span class="name">Corvell<br>Health</span>
    </div>
    <div class="letter">
      <p>I want to welcome you to our website. We are so happy you have taken a moment to visit us and learn about what we can do to help you. After all, that is why we have been here for over 40 years.</p>
      <p>First thing you should know is that all of <strong>our doctors and therapists are experts in their field.</strong> If you take a moment scroll through some of their names and bios and get to know them much better.</p>
      <p>As diverse as our specialists are, so are our services. We literally have everything you need at one location to get better and feel better quickly... all without surgery or other invasive treatments. While our staff may include an orthopedic surgeon, we have dedicated ourselves to non-surgical care. That means we do everything to keep you out of surgery... and if you have had surgery...we do everything we can to make sure you have the fastest and most complete recovery you can... so you never need it again.</p>
      <p>If you run through some of our services you can see the details of all the specialties that we offer.</p>
      <p>Take a look at some of the great things our patients have said about us. Yes... some of these patients are celebrities, but most are people just like you and I. If you take a minute to browse their comments, I think you will be really impressed.</p>
      <p>Finally, I want to tell you how easy it is to get the results you are looking for. It's really just three easy steps. First, you make an appointment to see one of our great doctors. They will sit down with you, one on one, and really listen to your problems. Then... our professional team works together <strong>to create a customized treatment plan just for you.</strong></p>
      <p>Here is where the fun part starts! Once we have a plan, we begin the process of getting you to feel better. This is where we excel. Our unique treatment programs are <strong>designed to get results faster by combining the best of each speciality.</strong> The result is we can keep you feeling good for years to come.... Again, without surgery or invasive procedures.</p>
      <p class="narrow">So there you have it. I hope you take a moment to call us so we can start the process of helping you achieve the health and vitality that you deserve.</p>
    </div>
    <p class="signoff"><span class="sig-name">Dr. Evan Marlowe,</span><span class="sig-role">Clinic Director</span></p>
    <div class="badges">
      <span class="badge shield"></span><span class="badge bar"></span>
      <span class="badge bar"></span>
      <span class="badge round"></span><span class="badge bar"></span>
      <span class="badge square"></span>
    </div>
    <div class="portrait" role="img" aria-label="Portrait photograph of the clinic director in a white coat"></div>
  </section>

  <!-- Services page -->
  <section class="page services-page">
    <svg class="bg" viewBox="0 0 573 443">
      <defs>
        <linearGradient id="goldBand3" x1="0" y1="0" x2="1" y2="0">
          <stop offset="0" stop-color="#c98a24"/>
          <stop offset=".4" stop-color="#f0c462"/>
          <stop offset="1" stop-color="#b97a1c"/>
        </linearGradient>
      </defs>
      <path d="M0,60 C70,140 180,150 300,110 S480,40 573,68 L573,0 L0,0Z" fill="url(#goldBand3)"/>
      <path d="M0,60 C70,110 180,120 300,80 S480,30 573,52 L573,0 L0,0Z" fill="var(--navy)"/>
    </svg>
    <h2 class="services-title">Services</h2>
    <div class="brand inner-brand">
      <span class="dot"></span>
      <span class="name">Corvell<br>Health</span>
    </div>
    <div class="service service-1">
      <h3>Services</h3>
      <p>We strive to provide complete care for our patients.<br>Learn more about all the services we provide.</p>
    </div>
    <div class="service service-2">
      <h3>Make An Appointment</h3>
      <p>We will do our best to accommodate your busy schedule.<br>Schedule an appointment today!</p>
    </div>
    <div class="service service-3">
      <h3>Online Forms</h3>
      <p>Our patient forms are available online so they can<br>be completed in the convenience of your own home or office.</p>
    </div>
    <div class="services-photo" role="img" aria-label="Photograph of a therapist treating a seated patient's neck beside a spine model"></div>
    <div class="url-band">
      <svg viewBox="0 0 180 14" width="180" height="14"><path d="M8,0 H180 V14 H0Z" fill="var(--navy)"/></svg>
      <span>www.CorvellHX.com</span>
    </div>
  </section>

</div>
</body>
</html>
```